Vitamin/Dietary Supplement Company needs a simple Hemp CBD Health retail website to display a few...

We need a simple website designed that will allow us to display a few products for purchase. We are a vitamin/dietary supplement company that wants to set up a separate website for CBD health products. CBD is a chemical compound found in hemp and cannabis plants that provide various health and medicinal benefits. Our target audience are individuals that suffer from health issues and would like to treat their pain relief with CBD as an alternative to prescription medication and over the counter drugs such as Paxorin and Lumex. Looking for a simple and clean website that is easy for customers to navigate and purchase products.

Target Market(s)

Our target audience are individuals that suffer from health issues and would like to treat their pain relief with CBD as an alternative to prescription medication and over the counter drugs such as Paxorin and Lumex.

Coding

Coded - Design and coding required

Font styles to use
Serif

Colors

Designer to choose colors to be used in the design.

Requirements
Nice to have
• Homepage, About page, FAQ page, Contact page, Blog page

```html
<!DOCTYPE html>
<html lang="en">
<head>
<meta charset="utf-8">
<title>Verdant Leaf – Hemp Extracts</title>
<link rel="stylesheet" href="https://fonts.googleapis.com/css2?family=Montserrat:wght@400;600;700;800&family=Roboto:wght@400;500;700&family=Oswald:wght@500&display=swap">
<style>
:root{
  --green:#6cb423;
  --green-light:#8fd03a;
  --green-dark:#4f8c14;
  --mint:#eef6dc;
  --ink:#111;
  --text:#333;
  --muted:#777;
  --white:#fff;
  --black:#050505;
  --soil:#4a3322;
}
*{box-sizing:border-box;margin:0;padding:0}
html,body{width:1200px;height:3711px;overflow:hidden}
body{position:relative;background:var(--white);font-family:'Roboto',sans-serif;color:var(--text)}
.abs{position:absolute}

/* top bar */
.topbar{left:0;top:0;width:1200px;height:30px;background:var(--green);color:var(--white);font-size:12px;display:flex;align-items:center;justify-content:space-between;padding:0 141px}
.topbar span{margin-right:18px;display:inline-flex;align-items:center;gap:5px}
.header{left:0;top:30px;width:1200px;height:69px;background:var(--white)}
.brand{left:141px;top:22px;display:flex;align-items:center;gap:10px;font-family:'Montserrat',sans-serif;font-weight:800;font-size:22px;color:var(--ink)}
.brand-dot{width:22px;height:22px;border-radius:50%;background:var(--green)}
.nav{left:440px;top:0;height:69px;display:flex;font-family:'Montserrat',sans-serif;font-size:13px;font-weight:600;color:var(--ink)}
.nav a{display:flex;align-items:center;padding:0 16px;color:inherit;text-decoration:none}
.nav a.active{background:var(--green);color:var(--white);width:60px;justify-content:center;padding:0}

/* hero */
.hero-photo{left:0;top:99px;width:1200px;height:495px;background:linear-gradient(90deg,#5a6b2a 0%,#2f4a1a 35%,#1c3512 60%,#2d4c1d 100%)}
.hero-photo::after{content:"";position:absolute;left:0;bottom:0;width:100%;height:80px;background:linear-gradient(#c9c6bd,#e6e3dc)}
.hero-title{left:560px;top:220px;width:560px;text-align:center;color:var(--white);font-family:'Montserrat',sans-serif;font-weight:800;font-size:50px;letter-spacing:1px}
.hero-sub{left:560px;top:290px;width:560px;text-align:center;color:var(--white);font-family:'Montserrat',sans-serif;font-weight:700;font-size:33px;letter-spacing:2px}
.btn-green{background:var(--green-light);color:var(--white);border-radius:30px;font-family:'Montserrat',sans-serif;font-weight:700;display:flex;align-items:center;justify-content:center}
.hero-btn{left:737px;top:354px;width:173px;height:44px;font-size:17px}

/* feature cards */
.card{top:594px;width:218px;height:289px;background:linear-gradient(var(--green-light),var(--green));color:var(--white);text-align:center}
.card svg{position:absolute;left:72px;top:17px}
.card h3{position:absolute;top:112px;width:100%;font-family:'Montserrat',sans-serif;font-size:16px;font-weight:700}
.card p{position:absolute;top:150px;left:22px;width:174px;font-size:12.5px;line-height:17px}
.card .more{position:absolute;left:47px;top:230px;width:124px;height:34px;border-radius:20px;font-family:'Montserrat',sans-serif;font-weight:700;font-size:14px;display:flex;align-items:center;justify-content:center}
.more.solid{background:var(--white);color:var(--ink)}
.more.outline{border:2px solid var(--white);color:var(--white)}

/* section heads */
.emblem{width:28px;height:22px;border-radius:4px;background:#444}
.sec-title{left:0;width:1200px;text-align:center;font-family:'Montserrat',sans-serif;font-weight:800;font-size:36px;color:var(--ink);letter-spacing:1px}
.sec-title em{font-style:normal;color:var(--green)}
.sec-sub{left:0;width:1200px;text-align:center;font-family:'Montserrat',sans-serif;font-size:15px;color:var(--muted);letter-spacing:2px}
.divider{left:520px;width:160px;height:2px;background:var(--green)}
.divider::after{content:"";position:absolute;left:70px;top:-7px;width:20px;height:14px;border-radius:50%;background:var(--green)}

/* products */
.arrow{width:26px;height:26px;border-radius:50%;background:#333;color:var(--white);font-size:16px;display:flex;align-items:center;justify-content:center}
.product{top:1163px;width:200px;text-align:center}
.bottle{margin:0 auto;width:74px;height:227px;border-radius:10px 10px 8px 8px;background:linear-gradient(#2a1d15,#4d6b24)}
.product h4{margin-top:24px;font-family:'Oswald',sans-serif;font-weight:500;font-size:17px;color:var(--green)}
.product p{margin-top:6px;font-size:11.5px;line-height:15px;color:var(--text)}
.price-row{margin:10px auto 0;width:150px;height:32px;display:flex;border:1px solid #ccc}
.price-row span{flex:1;display:flex;align-items:center;padding-left:8px;font-size:14px;color:var(--ink)}
.price-row b{width:55px;background:var(--green);color:var(--white);font-size:8.5px;font-weight:700;display:flex;align-items:center;justify-content:center}

/* science */
.science{left:0;top:1613px;width:1200px;height:807px;background:var(--mint)}
.lead{left:141px;width:918px;text-align:center;font-size:12.5px;line-height:18px;color:var(--ink)}
.fact{width:260px;font-size:12.5px;line-height:18px;color:var(--ink);padding:12px 0}
.fact.left{left:141px;border-left:5px solid var(--green);padding-left:18px}
.fact.right{left:799px;border-right:5px solid var(--green);padding-right:18px;text-align:right}
.fact.dark{border-color:var(--ink)}
.plant{left:482px;top:1937px;width:235px;height:290px;border-radius:8px;background:linear-gradient(#cfe3ad 0%,#7fae4a 55%,#6b5a3c 85%,var(--soil) 100%)}
.sci-btn{left:527px;top:2288px;width:146px;height:33px;font-size:14px}

/* process */
.step-num{width:50px;height:50px;border-radius:50%;background:var(--ink);color:var(--white);font-family:'Montserrat',sans-serif;font-weight:700;font-size:22px;display:flex;align-items:center;justify-content:center}
.step-line{top:2734px;height:1px;background:#ccc}
.step-box{top:2820px;width:292px;height:188px;border:2px solid var(--green);text-align:center}
.step-box h4{margin-top:50px;font-family:'Montserrat',sans-serif;font-weight:700;font-size:17px;color:var(--ink)}
.step-box p{margin:14px auto 0;width:220px;font-size:12.5px;line-height:17px;color:var(--ink)}
.step-box .btn-green{width:116px;height:32px;margin:14px auto 0;font-size:12.5px}
.step-icon{top:2780px;width:70px;height:60px;background:var(--white);display:flex;justify-content:center}
.step-icon div{width:56px;height:56px;border-radius:6px;background:linear-gradient(#d9e9bd,#6cb423)}

/* newsletter */
.newsletter{left:0;top:3080px;width:1200px;height:149px;background:var(--green);color:var(--white)}
.nl-icon{left:141px;top:50px;width:26px;height:22px;border:2px solid var(--white);border-radius:3px}
.nl-title{left:178px;top:44px;font-family:'Montserrat',sans-serif;font-size:26px}
.nl-text{left:178px;top:82px;font-family:'Montserrat',sans-serif;font-size:16px;line-height:25px;color:#f4ffd9}
.nl-input{left:604px;top:62px;width:252px;height:30px;background:var(--white);border-radius:16px 0 0 16px;font-size:11px;color:#999;padding:8px 16px}
.nl-btn{left:856px;top:62px;width:124px;height:30px;background:var(--black);border-radius:16px;font-family:'Montserrat',sans-serif;font-weight:700;font-size:13px;display:flex;align-items:center;justify-content:center}

/* footer */
.footer{left:0;top:3229px;width:1200px;height:482px;background:linear-gradient(var(--black) 0 50%,#0f2708 70%,#3f7a1c 100%);color:var(--white)}
.foot-brand{left:141px;top:147px;display:flex;align-items:center;gap:8px;font-family:'Montserrat',sans-serif;font-weight:800;font-size:20px}
.foot-about{left:141px;top:180px;width:210px;font-size:12.5px;line-height:19px}
.foot-h{font-family:'Montserrat',sans-serif;font-weight:700;font-size:13px;letter-spacing:1px}
.links{left:396px;top:130px;list-style:none;font-size:11px;line-height:28px}
.links li::before{content:"▸ ";font-size:9px}
.field{left:601px;width:230px;height:32px;border:1px solid #ccc;border-radius:4px;font-size:11px;padding:8px;color:#ddd}
.send{left:601px;top:254px;width:115px;height:30px;font-size:13px}
.contact{left:871px;font-size:11.5px;line-height:17px;display:flex;gap:12px;align-items:flex-start}
.contact svg{flex:none;margin-top:2px}
.social{left:895px;top:268px;display:flex;gap:12px}
.social i{width:12px;height:12px;border-radius:50%;background:var(--white)}
</style>
</head>
<body>

<div class="abs topbar">
  <div>
    <span><svg width="11" height="11" viewBox="0 0 12 12" fill="#fff"><path d="M2 1h3l1 3-2 1a7 7 0 0 0 3 3l1-2 3 1v3c0 1-1 1-1 1A10 10 0 0 1 1 2s0-1 1-1z"/></svg>+000 555 0142</span>
    <span><svg width="12" height="9" viewBox="0 0 12 9" fill="none" stroke="#fff"><rect x=".5" y=".5" width="11" height="8"/><path d="M.5.5 6 5l5.5-4.5"/></svg>hello@verdantleaf.example</span>
  </div>
  <div>
    <span>LOGIN | REGISTER</span>
    <span><svg width="13" height="11" viewBox="0 0 13 11" fill="none" stroke="#fff" stroke-width="1.4"><path d="M0 1h2l2 6h6l2-5H3"/><circle cx="5" cy="9.5" r="1"/><circle cx="9" cy="9.5" r="1"/></svg>0</span>
  </div>
</div>
<header class="abs header">
  <div class="abs brand"><span class="brand-dot"></span>VERDANT LEAF</div>
  <nav class="abs nav">
    <a class="active">HOME</a><a>PRODUCTS</a><a>OUR STORY</a><a>QUALITY CONTROL</a><a>WHOLESALE</a><a>CONTACT US</a>
  </nav>
</header>

<div class="abs hero-photo" role="img" aria-label="Glass jar of hemp oil beside hemp leaves on a wooden table"></div>
<h1 class="abs hero-title">HEMP EXTRACTS</h1>
<div class="abs hero-sub">CRAFTED WITH CARE</div>
<div class="abs btn-green hero-btn">SHOP NOW</div>

<div class="abs card" style="left:141px">
  <svg width="74" height="74" viewBox="0 0 74 74" fill="none" stroke="#fff" stroke-width="3"><circle cx="37" cy="37" r="34"/><path d="M20 26h6l5 18h18l4-13H28" stroke-linejoin="round"/><circle cx="33" cy="50" r="2.5"/><circle cx="47" cy="50" r="2.5"/></svg>
  <h3>Shop CBD</h3>
  <p>Lorem ipsum dolor sit amet, consectetuer adipiscing elit, sed diam nonummy nibh</p>
  <div class="more solid">Read More</div>
</div>
<div class="abs card" style="left:375px">
  <svg width="74" height="74" viewBox="0 0 74 74" fill="none" stroke="#fff" stroke-width="3"><circle cx="37" cy="37" r="34"/><path d="M37 52 22 37a8 8 0 0 1 15-10 8 8 0 0 1 15 10z" stroke-linejoin="round"/></svg>
  <h3>CBD Benefits</h3>
  <p>Lorem ipsum dolor sit amet, consectetuer adipiscing elit, sed diam nonummy nibh</p>
  <div class="more outline">Read More</div>
</div>
<div class="abs card" style="left:609px">
  <svg width="74" height="74" viewBox="0 0 74 74" fill="none" stroke="#fff" stroke-width="3"><circle cx="37" cy="37" r="34"/><path d="M29 29a8 8 0 1 1 12 7c-3 2-4 3-4 7"/><circle cx="37" cy="51" r="1.5" fill="#fff"/></svg>
  <h3>Common Questions</h3>
  <p>Lorem ipsum dolor sit amet, consectetuer adipiscing elit, sed diam nonummy nibh</p>
  <div class="more outline">Read More</div>
</div>
<div class="abs card" style="left:843px">
  <svg width="74" height="74" viewBox="0 0 74 74" fill="none" stroke="#fff" stroke-width="3"><circle cx="37" cy="37" r="34"/><path d="M24 38l9 9 17-19" stroke-linecap="round"/></svg>
  <h3>Legally Compliant</h3>
  <p>Lorem ipsum dolor sit amet, consectetuer adipiscing elit, sed diam nonummy nibh</p>
  <div class="more outline">Read More</div>
</div>

<div class="abs emblem" style="left:586px;top:970px" role="img" aria-label="Small hemp emblem"></div>
<h2 class="abs sec-title" style="top:1012px">OUR <em>PRODUCTS</em></h2>
<div class="abs sec-sub" style="top:1064px">WHAT WE OFFER</div>
<div class="abs divider" style="top:1106px"></div>

<div class="abs arrow" style="left:111px;top:1274px">‹</div>
<div class="abs arrow" style="left:1061px;top:1274px">›</div>

<div class="abs product" style="left:182px">
  <div class="bottle" role="img" aria-label="Classic hemp oil dropper bottle"></div>
  <h4>CLASSIC</h4>
  <p>240mg Full Spectrum CBD<br>Oil, High Grade Hemp Extract<br>(50mg/ml)</p>
  <div class="price-row"><span>$ 38.50</span><b>SHOP NOW</b></div>
</div>
<div class="abs product" style="left:410px">
  <div class="bottle" role="img" aria-label="Signature hemp oil dropper bottle"></div>
  <h4>SIGNATURE</h4>
  <p>725mg Full Spectrum CBD<br>Oil, High Grade Hemp Extract<br>(50mg/ml)</p>
  <div class="price-row"><span>$ 99.00</span><b>SHOP NOW</b></div>
</div>
<div class="abs product" style="left:637px">
  <div class="bottle" role="img" aria-label="Classic hemp oil dropper bottle"></div>
  <h4>CLASSIC</h4>
  <p>240mg Full Spectrum CBD<br>Oil, High Grade Hemp Extract<br>(50mg/ml)</p>
  <div class="price-row"><span>$ 38.50</span><b>SHOP NOW</b></div>
</div>
<div class="abs product" style="left:865px">
  <div class="bottle" role="img" aria-label="Signature hemp oil dropper bottle"></div>
  <h4>SIGNATURE</h4>
  <p>725mg Full Spectrum CBD<br>Oil, High Grade Hemp Extract<br>(50mg/ml)</p>
  <div class="price-row"><span>$ 99.00</span><b>SHOP NOW</b></div>
</div>

<section class="abs science"></section>
<div class="abs emblem" style="left:574px;top:1680px" role="img" aria-label="Small hemp emblem"></div>
<h2 class="abs sec-title" style="top:1733px">SCIENCE <em>BEHIND CANNABIS</em></h2>
<p class="abs lead" style="top:1818px">Lorem ipsum dolor sit amet, consectetuer adipiscing elit, sed diam nonummy nibh euismod tincidunt ut laoreet dolore magna aliquam erat volutpat. Ut wisi enim ad minim veniam, quis nostrud exerci tation ullamcorper suscipit lobortis nisl ut aliquip ex ea commodo consequat. Duis autem vel eum iriure dolor in hendrerit in vulputate velit esse molestie consequat.</p>

<p class="abs fact left" style="top:1925px">Lorem ipsum dolor sit amet, consectetuer adipiscing elit, sed diam nonummy nibh aliquam erat volutpat.</p>
<p class="abs fact left dark" style="top:2053px">Lorem ipsum dolor sit amet, consectetuer adipiscing elit, sed diam nonummy nibh aliquam erat volutpat.</p>
<p class="abs fact left" style="top:2187px">Lorem ipsum dolor sit amet, consectetuer adipiscing elit, sed diam nonummy nibh aliquam erat volutpat.</p>
<p class="abs fact right" style="top:1925px">Lorem ipsum dolor sit amet, consectetuer adipiscing elit, sed diam nonummy nibh aliquam erat volutpat.</p>
<p class="abs fact right dark" style="top:2053px">Lorem ipsum dolor sit amet, consectetuer adipiscing elit, sed diam nonummy nibh aliquam erat volutpat.</p>
<p class="abs fact right" style="top:2187px">Lorem ipsum dolor sit amet, consectetuer adipiscing elit, sed diam nonummy nibh aliquam erat volutpat.</p>

<div class="abs plant" role="img" aria-label="Photo of a young cannabis plant growing from a mound of soil"></div>
<div class="abs btn-green sci-btn">READ MORE</div>

<div class="abs emblem" style="left:586px;top:2500px" role="img" aria-label="Small hemp emblem"></div>
<h2 class="abs sec-title" style="top:2545px">HOW <em>WE DO IT</em></h2>
<div class="abs divider" style="top:2600px"></div>
<p class="abs lead" style="top:2625px">Lorem ipsum dolor sit amet, consectetuer adipiscing elit, sed diam nonummy nibh euismod tincidunt ut laoreet dolore magna aliquam erat volutpat. Ut wisi enim ad minim veniam, quis nostrud exerci tation ullamcorper suscipit lobortis nisl ut aliquip ex ea commodo consequat.</p>

<div class="abs step-line" style="left:312px;width:264px"></div>
<div class="abs step-line" style="left:626px;width:262px"></div>
<div class="abs step-num" style="left:262px;top:2709px">1</div>
<div class="abs step-num" style="left:576px;top:2709px">2</div>
<div class="abs step-num" style="left:888px;top:2709px">3</div>

<div class="abs step-box" style="left:141px"><h4>FARMING</h4><p>Lorem ipsum dolor sit amet, consectetuer aliquam erat volutpat.</p><div class="btn-green">READ MORE</div></div>
<div class="abs step-box" style="left:455px"><h4>EXTRACTION</h4><p>Lorem ipsum dolor sit amet, consectetuer aliquam erat volutpat.</p><div class="btn-green">READ MORE</div></div>
<div class="abs step-box" style="left:767px"><h4>MANUFACTURING</h4><p>Lorem ipsum dolor sit amet, consectetuer aliquam erat volutpat.</p><div class="btn-green">READ MORE</div></div>
<div class="abs step-icon" style="left:252px"><div role="img" aria-label="Farmer and tractor illustration"></div></div>
<div class="abs step-icon" style="left:566px"><div role="img" aria-label="Extraction equipment illustration"></div></div>
<div class="abs step-icon" style="left:878px"><div role="img" aria-label="Factory worker illustration"></div></div>

<section class="abs newsletter">
  <div class="abs nl-icon"></div>
  <div class="abs nl-title">Newsletter Subscribe</div>
  <div class="abs nl-text">Join our mailing list and save<br>10% off 1st orders!</div>
  <div class="abs nl-input">Enter your email address</div>
  <div class="abs nl-btn">SUBSCRIBE</div>
</section>

<footer class="abs footer" role="img" aria-label="Footer with hemp field growing along the bottom edge">
  <div class="abs foot-brand"><span class="brand-dot"></span>VERDANT LEAF</div>
  <p class="abs foot-about">CBD oil, derived from agricultural hemp, has been widely recognized for many benefits on human health.</p>

  <div class="abs foot-h" style="left:396px;top:84px">QUICK LINKS</div>
  <div class="abs" style="left:396px;top:104px;width:40px;height:1px;background:#fff"></div>
  <ul class="abs links"><li>HOME</li><li>PRODUCTS</li><li>OUR STORY</li><li>QUALITY CONTROL</li><li>WHOLESALE</li><li>CONTACT US</li></ul>

  <div class="abs foot-h" style="left:601px;top:84px">GET IN TOUCH</div>
  <div class="abs field" style="top:128px">Name</div>
  <div class="abs field" style="top:170px">Email</div>
  <div class="abs field" style="top:212px">Message</div>
  <div class="abs btn-green send">SEND</div>

  <div class="abs foot-h" style="left:871px;top:84px">CONTACT DETAILS</div>
  <div class="abs contact" style="top:130px"><svg width="10" height="14" viewBox="0 0 10 14" fill="#fff"><path d="M5 0a5 5 0 0 1 5 5c0 4-5 9-5 9S0 9 0 5a5 5 0 0 1 5-5zm0 3a2 2 0 1 0 0 4 2 2 0 0 0 0-4z"/></svg><span>2210 Fernhill Ave #4B<br>Mesa Verde, AZ 85000</span></div>
  <div class="abs contact" style="top:187px"><svg width="11" height="11" viewBox="0 0 12 12" fill="#fff"><path d="M2 1h3l1 3-2 1a7 7 0 0 0 3 3l1-2 3 1v3c0 1-1 1-1 1A10 10 0 0 1 1 2s0-1 1-1z"/></svg><span>(000) 555 0187</span></div>
  <div class="abs contact" style="top:222px"><svg width="12" height="9" viewBox="0 0 12 9" fill="none" stroke="#fff"><rect x=".5" y=".5" width="11" height="8"/><path d="M.5.5 6 5l5.5-4.5"/></svg><span>hello@verdantleaf.example</span></div>
  <div class="abs social"><i></i><i></i><i></i><i></i></div>
</footer>

</body>
</html>
```